marcel's mobile mechanic

a business card that will get attention from clients
- name of the business: M'S MOBILE MECHANIC
- we currently do not have a logo and do not need one at the moment, happy for the designers to just put the business name on the card using appropriate fonts

Target Market(s)

low cost mobile repairs

Industry/Entity Type

Business

Contact Information for Business Card

attracts customers

Font styles to use
Sans Serif

Colors
0255a3
fbee3d
000000

Requirements
Must have
• (555) 318-4907
• Marcel Treviño
• for lower income target market
Nice to have
• "we save you money"
• Easy to read
Should not have
• nothing comes to mind

```html
<!DOCTYPE html>
<html lang="en">
<head>
<meta charset="utf-8">
<title>M'S Mobile Mechanic — Business Card</title>
<link rel="stylesheet" href="https://fonts.googleapis.com/css2?family=Roboto:ital,wght@0,400;0,700;1,400&display=swap">
<style>
  :root {
    --navy: #0b2d5f;
    --orange: #f28a1c;
    --ink: #3c3f44;
    --paper: #ffffff;
    --backdrop: #e7e5e1;
    --line-light: #c9d3e2;
  }
  * { box-sizing: border-box; margin: 0; padding: 0; }
  html, body { width: 1200px; height: 911px; overflow: hidden; }
  body {
    background: var(--backdrop);
    font-family: "Roboto", Arial, sans-serif;
    display: flex;
    align-items: center;
    justify-content: center;
    gap: 90px;
  }
  .card {
    width: 400px;
    height: 690px;
    position: relative;
    overflow: hidden;
    box-shadow: 0 12px 30px rgba(0,0,0,.18);
  }

  /* Business name, set as plain text */
  .business-name {
    font-weight: 700;
    white-space: nowrap;
  }

  /* Front */
  .card-front { background: var(--paper); }
  .card-front .business-name {
    position: absolute;
    top: 190px;
    left: 0; right: 0;
    text-align: center;
    color: var(--navy);
    font-size: 30px;
  }
  .contact {
    position: absolute;
    left: 48px;
    top: 400px;
    display: flex;
    gap: 14px;
  }
  .contact-icons {
    display: flex;
    flex-direction: column;
    width: 18px;
    padding-top: 2px;
  }
  .contact-icons svg { width: 15px; height: 15px; fill: var(--navy); }
  .contact-icons .icon-person { margin-bottom: 50px; }
  .contact-icons .icon-pin { margin-bottom: 42px; }
  .contact-icons .icon-phone,
  .contact-icons .icon-mail,
  .contact-icons .icon-web { margin-bottom: 6px; }
  .divider { width: 12px; height: 200px; }
  .details { padding-top: 8px; }
  .person-name {
    color: var(--navy);
    font-weight: 700;
    font-size: 22px;
    text-transform: uppercase;
    letter-spacing: .3px;
  }
  .person-role {
    color: var(--orange);
    font-size: 16px;
    text-transform: uppercase;
    margin-bottom: 18px;
  }
  .details p {
    color: var(--ink);
    font-size: 16px;
    line-height: 1.35;
  }
  .address { margin-bottom: 12px; }

  /* Back: landscape layout turned onto the portrait card */
  .card-back { background: var(--navy); }
  .back-layout {
    position: absolute;
    width: 690px;
    height: 400px;
    left: -145px;
    top: 145px;
    transform: rotate(90deg);
    display: flex;
    flex-direction: column;
    align-items: center;
    justify-content: center;
    gap: 22px;
  }
  .card-back .business-name {
    color: var(--paper);
    font-size: 40px;
  }
  .tagline {
    order: 2;
    display: flex;
    align-items: center;
    gap: 12px;
    color: var(--paper);
    font-size: 16px;
    font-style: italic;
    white-space: nowrap;
  }
  .tagline::before,
  .tagline::after {
    content: "";
    display: block;
    width: 60px;
    height: 1px;
    background: var(--line-light);
  }
</style>
</head>
<body>

  <section class="card card-front" aria-label="Business card front">
    <h1 class="business-name">M'S Mobile Mechanic</h1>

    <div class="contact">
      <div class="contact-icons" aria-hidden="true">
        <svg class="icon-person" viewBox="0 0 16 16"><circle cx="8" cy="4.5" r="3.5"/><path d="M1 16c0-4 3-6.5 7-6.5s7 2.5 7 6.5z"/></svg>
        <svg class="icon-pin" viewBox="0 0 16 16"><path d="M8 0a5.5 5.5 0 0 0-5.5 5.5C2.5 10 8 16 8 16s5.5-6 5.5-10.5A5.5 5.5 0 0 0 8 0zm0 8a2.4 2.4 0 1 1 0-4.8A2.4 2.4 0 0 1 8 8z"/></svg>
        <svg class="icon-phone" viewBox="0 0 16 16"><path d="M3.6 1 6 3.6 4.7 5.4a10 10 0 0 0 5.9 5.9L12.4 10 15 12.4l-1.6 2.4C7.2 15 1 8.8 1.2 2.6z"/></svg>
        <svg class="icon-mail" viewBox="0 0 16 16"><path d="M1 3h14v10H1z"/><path d="M1 3l7 6 7-6" fill="none" stroke="#fff" stroke-width="1.3"/></svg>
        <svg class="icon-web" viewBox="0 0 16 16"><circle cx="8" cy="8" r="7"/><path d="M1 8h14M8 1c-3 3.5-3 10.5 0 14M8 1c3 3.5 3 10.5 0 14" fill="none" stroke="#fff" stroke-width="1"/></svg>
      </div>

      <svg class="divider" viewBox="0 0 12 200" aria-hidden="true">
        <rect x="4.5" y="8" width="3" height="184" fill="#f28a1c"/>
        <circle cx="6" cy="6" r="5" fill="none" stroke="#f28a1c" stroke-width="2.5"/>
        <circle cx="6" cy="194" r="5" fill="none" stroke="#f28a1c" stroke-width="2.5"/>
      </svg>

      <div class="details">
        <h2 class="person-name">Marcel Treviño</h2>
        <p class="person-role">CEO/Founder</p>
        <p class="address">214 Alder Creek Road<br>Willowbrook, Alaska 99871</p>
        <p>(555) 318-4907<br>hello@msmobilemech.com<br>www.msmobilemech.com</p>
      </div>
    </div>
  </section>

  <section class="card card-back" aria-label="Business card back">
    <div class="back-layout">
      <h2 class="business-name">M'S Mobile Mechanic</h2>
      <p class="tagline">For lower income target market</p>
    </div>
  </section>

</body>
</html>
```